Erstellung eines responsiven One-Pagers für mittelständiges Unternehmen im Bauhauptgewerbe
Zielgruppe
Seit fast 30 Jahren sind wir als mittelständiges Unternehmen im Bauhauptgewerbe tätig.
Aufgabenstellung
Die bestehende Webseite soll einen Relaunch bekommen. Dazu entnehmen Sie bitte Bildmaterial und Logo aus der alten Seite. Wir würden gerne daraus einen responsiven One-Pager bauen.
Da die alte Seite jetzt schon 10 Jahre alt ist, würden wir gerne ein neues Design erstellen lassen. Später werden wir es entweder selbst von unserem Programmierer entwickeln lassen oder Sie erstellen uns ein Angebot. Das Design sollte auch so aufgebaut sein, dass es responsive funktionieren würde.

```html
<!DOCTYPE html>
<html lang="de">
<head>
<meta charset="utf-8">
<title>Hartwerk Bau</title>
<link href="https://fonts.googleapis.com/css2?family=Fira+Sans:ital,wght@0,400;0,500;0,700;1,500&family=Fira+Sans+Condensed:wght@500;600&display=swap" rel="stylesheet">
<style>
:root{
  --navy:#1b2d57;
  --navy-dark:#142346;
  --blue:#2d58aa;
  --line:#3a4f7c;
  --white:#ffffff;
  --text:#26324d;
  --muted:#5d6680;
  --page:#ffffff;
  --divider:#c9ccd4;
}
*{margin:0;padding:0;box-sizing:border-box}
html,body{width:1200px;height:900px;overflow:hidden;background:var(--page)}
body{font-family:"Fira Sans",sans-serif;color:var(--text)}
.site-header{height:100px;display:flex;align-items:center;background:var(--white);border-bottom:6px solid var(--blue)}
.brand{width:430px;display:flex;justify-content:flex-end;align-items:center;padding-right:40px;border-right:2px solid var(--divider);height:62px}
.brand-name{font-family:"Fira Sans",sans-serif;font-weight:500;font-size:22px;color:var(--navy)}
.tagline{padding-left:28px;font-style:italic;font-weight:500;font-size:15px;color:var(--navy)}
.main-nav{height:58px;background:var(--navy);display:flex;align-items:stretch;padding-left:140px}
.nav-item{width:142px;display:flex;align-items:center;justify-content:center;font-family:"Fira Sans Condensed",sans-serif;font-weight:600;font-size:14px;color:var(--white);border-left:1px solid var(--line)}
.nav-item:last-of-type{border-right:1px solid var(--line)}
.contact-bar{margin-left:auto;padding-right:80px;display:flex;align-items:center;gap:8px;font-size:10.5px;color:var(--white)}
.contact-bar svg{width:11px;height:11px;fill:var(--white);vertical-align:-1px;margin-right:3px}
.contact-sep{opacity:.7}
.hero{position:relative;height:362px;background:linear-gradient(180deg,#7d9bcf 0%,#b8c8df 30%,#cfd3d6 55%,#9aa0a4 100%);border-bottom:6px solid var(--blue)}
.slider-nav{position:absolute;left:540px;bottom:14px;display:flex;align-items:center;gap:10px;font-size:13px;font-weight:700;color:var(--white)}
.slider-nav svg{width:10px;height:16px;fill:var(--navy)}
.slide-dot.is-active{background:var(--navy);padding:1px 5px}
.section{padding-top:26px}
.section-title-bar{position:relative;height:10px;background:var(--navy);margin-top:8px}
.section-title{position:absolute;left:270px;top:-9px;background:var(--white);padding:0 16px;font-family:"Fira Sans Condensed",sans-serif;font-weight:600;font-size:22px;color:var(--navy);line-height:28px}
.section-body{display:flex;gap:36px;padding:22px 0 0 286px}
.section-text{width:394px}
.section-sub{font-size:13px;font-weight:700;color:var(--navy);margin-bottom:22px}
.lead{font-size:11.5px;font-weight:500;margin-bottom:14px}
.section-text p{font-size:10.5px;line-height:1.55;color:var(--muted);margin-bottom:12px}
.section-image{width:220px;height:130px;margin-top:22px;border:4px solid #dfe2e8;background:linear-gradient(160deg,#8b8f93,#6e6a64 60%,#4d5a66)}
</style>
</head>
<body>
<header class="site-header">
  <div class="brand"><span class="brand-name">Hartwerk Bau</span></div>
  <p class="tagline">Seit über 20 Jahren: Betoninstandsetzung | Spritzbeton | Brückensanierung | Balkone | Abdichtung</p>
</header>
<nav class="main-nav">
  <a class="nav-item">UNTERNEHMEN</a>
  <a class="nav-item">REFERENZEN</a>
  <a class="nav-item">LEISTUNGEN</a>
  <a class="nav-item">KONTAKT</a>
  <div class="contact-bar">
    <span><svg viewBox="0 0 24 24"><path d="M6.6 10.8a15 15 0 0 0 6.6 6.6l2.2-2.2a1 1 0 0 1 1-.25 11.4 11.4 0 0 0 3.6.6 1 1 0 0 1 1 1V20a1 1 0 0 1-1 1A17 17 0 0 1 3 4a1 1 0 0 1 1-1h3.5a1 1 0 0 1 1 1c0 1.25.2 2.45.6 3.6a1 1 0 0 1-.25 1z"/></svg>(0 61 31) 48 27 15</span>
    <span class="contact-sep">|</span>
    <span><svg viewBox="0 0 24 24"><path d="M6 2h12v6H6zM4 9h16a2 2 0 0 1 2 2v6h-4v5H6v-5H2v-6a2 2 0 0 1 2-2zm4 7v4h8v-4z"/></svg>(0 61 31) 48 27 16</span>
    <span class="contact-sep">|</span>
    <span><svg viewBox="0 0 24 24"><path d="M2 5h20v14H2zm2 2v.5l8 5 8-5V7z"/></svg>kontakt@hartwerk-bau.de</span>
  </div>
</nav>
<section class="hero" role="img" aria-label="Foto der Firmenhalle mit Rolltor, Lieferwagen und Mitarbeitern unter blauem Himmel">
  <div class="slider-nav">
    <svg viewBox="0 0 10 16"><path d="M10 0v16L0 8z"/></svg>
    <span class="slide-dot is-active">1</span><span class="slide-dot">2</span><span class="slide-dot">3</span><span class="slide-dot">4</span>
    <svg viewBox="0 0 10 16"><path d="M0 0v16l10-8z"/></svg>
  </div>
</section>
<section class="section">
  <div class="section-title-bar"><h2 class="section-title">UNTERNEHMEN</h2></div>
  <div class="section-body">
    <div class="section-text">
      <h3 class="section-sub">Betonsanierung in Heidelberg, Mannheim und Umgebung</h3>
      <p class="lead">Langfristige Betonerhaltung durch Instandsetzung und Korrosionsschutz</p>
      <p>Sie sind richtig bei uns, wenn wir über folgende Begriffe sprechen: Betonschäden, Balkonschäden, Betonschutz und Instandsetzung, Betonkosmetik, Betonsanierung, Balkone, Brücken, Brandschutz, SPCC und Spritzbeton.</p>
      <p>Als Untergrundvorbereitung, bei jeder Instandhaltungsmaßnahme, ist eine Reinigung erforderlich. Hierfür kommen das Sandstrahlen, Druckluftstrahlen, Wasserstrahlen, Fräsen oder Schleifen zum Einsatz.</p>
    </div>
    <div class="section-image" role="img" aria-label="Foto einer Betonsanierung an einer Baustelle"></div>
  </div>
</section>
</body>
</html>
```